BrivoMetra. Lantern for the Enterprise Worth. Business card

Professional business card for BrivoMetra (Lantern for the Enterprise Worth)
My rationale: Strategy-> Execution-> Results-> Value that lead to the BrivoMetra name: We put the Lantern for the Enterprise Worth.
We deliver value to our customers helping them at defining a good strategy (cyan arrow). 90% of well formulated strategies fail due to poor execution so we also consider strategical execution very important (green arrow). Due to the execution we obtain the results (blue arrow). Finally, the results provide feedback to redefine strategy, and the new strategy has to be executed and new results obtained providing new feedback and on and on. It's like a wheel that finally, must create corporate value: value for shareholders, staholders, employees, providers...-

Target Market(s)

CEOs and steering comitees , invewrnent funds

Industry/Entity Type

Business Consultant

Contact Information for Business Card

Teodoro Vinschetti
CEO & Founder
teodoro.vinschetti@brivometra-example.com
Mobile: +34 655.802.913
www.brivometra-example.com

Colors

Designer to choose colors to be used in the design.

Requirements
Nice to have
• Nice to hace the words: Strategy, execution, results
• Nice to vave the claim: Lantern for the Enterprise Worth
• The three colors should be shown:
• cyan for STRATEGY
• green for EXECUTION
• blue for RESULTS
Should not have
• Complete black background

```html
<!DOCTYPE html>
<html lang="en">
<head>
<meta charset="UTF-8">
<title>BrivoMetra — Business Card</title>
<link rel="stylesheet" href="https://fonts.googleapis.com/css2?family=Open+Sans:wght@400;600;700;800&display=swap">
<style>
  :root {
    --navy: #243e8e;
    --green: #93c83e;
    --cyan: #29a9e1;
    --white: #ffffff;
    --ink: #2a2f45;
    --backdrop: #e4e6ea;
  }
  * { margin: 0; padding: 0; box-sizing: border-box; }
  html, body { width: 1200px; height: 900px; overflow: hidden; }
  body {
    background: var(--backdrop);
    font-family: "Open Sans", Arial, sans-serif;
    position: relative;
  }
  .card {
    position: absolute;
    left: 280px;
    width: 640px;
    height: 366px;
    overflow: hidden;
    box-shadow: 0 6px 18px rgba(0,0,0,0.18);
  }

  /* Front */
  .card-front { top: 64px; background: var(--navy); }
  .front-wordmark {
    position: absolute; top: 140px; left: 0; width: 100%;
    text-align: center; color: var(--white);
    font-weight: 800; font-size: 60px; letter-spacing: -1px;
  }
  .front-rule {
    position: absolute; top: 262px; left: 30px; width: 580px;
    height: 1.5px; background: var(--green);
  }
  .pillar {
    position: absolute; font-weight: 800; font-size: 17px; letter-spacing: 0.5px;
  }
  .pillar-strategy { top: 280px; left: 36px; color: var(--white); }
  .pillar-execution { top: 305px; left: 0; width: 100%; text-align: center; color: var(--green); }
  .pillar-results { top: 330px; right: 36px; color: var(--cyan); }

  /* Back */
  .card-back { top: 470px; background: var(--white); }
  .back-wordmark {
    position: absolute; top: 22px; left: 34px;
    color: var(--navy); font-weight: 800; font-size: 54px; letter-spacing: -1px;
  }
  .person-name {
    position: absolute; top: 112px; left: 40px;
    color: var(--navy); font-weight: 800; font-size: 23px; letter-spacing: 0.5px;
    text-transform: uppercase;
  }
  .person-role {
    position: absolute; top: 142px; left: 40px;
    color: var(--green); font-size: 16px;
  }
  .contact-list { position: absolute; top: 178px; left: 40px; list-style: none; }
  .contact-item {
    display: flex; align-items: center; gap: 10px;
    color: var(--ink); font-size: 15.5px; line-height: 26px;
  }
  .contact-icon { width: 16px; height: 16px; flex: none; }
  .back-rule {
    position: absolute; top: 266px; left: 40px; width: 560px;
    height: 1.5px; background: var(--green);
  }
  .tagline {
    position: absolute; top: 284px; left: 40px;
    color: var(--ink); font-size: 18px; text-transform: uppercase; letter-spacing: 0.3px;
  }
  .accent-bands { position: absolute; left: 0; bottom: 0; width: 640px; height: 40px; }
</style>
</head>
<body>

  <section class="card card-front" aria-label="Card front">
    <div class="front-wordmark">BrivoMetra</div>
    <div class="front-rule"></div>
    <div class="pillar pillar-strategy">STRATEGY</div>
    <div class="pillar pillar-execution">EXECUTION</div>
    <div class="pillar pillar-results">RESULTS</div>
  </section>

  <section class="card card-back" aria-label="Card back">
    <div class="back-wordmark">BrivoMetra</div>
    <div class="person-name">Teodoro Vinschetti</div>
    <div class="person-role">CEO &amp; Founder</div>
    <ul class="contact-list">
      <li class="contact-item">
        <svg class="contact-icon" viewBox="0 0 16 16" aria-hidden="true">
          <circle cx="8" cy="8" r="7" fill="none" stroke="#29a9e1" stroke-width="1.2"/>
          <path d="M5.5 4.5c.6-.4 1-.3 1.3.3l.5 1.1c.2.4 0 .7-.3 1l-.3.3c.4.9 1 1.5 1.9 1.9l.3-.3c.3-.3.6-.5 1-.3l1.1.5c.6.3.7.7.3 1.3-.6.9-1.6 1-2.6.5-1.6-.8-2.9-2.1-3.7-3.7-.5-1-.4-2 .5-2.6z" fill="#29a9e1"/>
        </svg>
        +34 655.802.913
      </li>
      <li class="contact-item">
        <svg class="contact-icon" viewBox="0 0 16 16" aria-hidden="true">
          <rect x="1.5" y="3.5" width="13" height="9" fill="none" stroke="#29a9e1" stroke-width="1.2"/>
          <path d="M1.5 3.5 8 9l6.5-5.5" fill="none" stroke="#29a9e1" stroke-width="1.2"/>
        </svg>
        teodoro.vinschetti@brivometra-example.com
      </li>
      <li class="contact-item">
        <svg class="contact-icon" viewBox="0 0 16 16" aria-hidden="true">
          <circle cx="8" cy="8" r="6.5" fill="none" stroke="#29a9e1" stroke-width="1.2"/>
          <ellipse cx="8" cy="8" rx="3" ry="6.5" fill="none" stroke="#29a9e1" stroke-width="1.1"/>
          <path d="M1.5 8h13M2.5 5h11M2.5 11h11" stroke="#29a9e1" stroke-width="1.1"/>
        </svg>
        www.brivometra-example.com
      </li>
    </ul>
    <div class="back-rule"></div>
    <div class="tagline">Lantern for the Enterprise Worth</div>
    <svg class="accent-bands" viewBox="0 0 640 40" aria-hidden="true">
      <polygon points="0,22 360,36 360,40 0,40" fill="#93c83e"/>
      <polygon points="378,14 600,14 580,40 348,40" fill="#243e8e"/>
    </svg>
  </section>

</body>
</html>
```